R & M Holdings of Fairhaven, LLC
“Steady Care for Every Home"
R & M Holdings of Fairhaven, LLC -
Creative Brief
Professional
Bertram Lasko
Property Manager
P.O. Box 38216 Goldsboro, NC 27534
rmholdings2011@quillpost.example

```html
<!DOCTYPE html>
<html lang="en">
<head>
<meta charset="utf-8">
<title>R &amp; M Holdings of Fairhaven, LLC — Business Cards</title>
<link rel="stylesheet" href="https://fonts.googleapis.com/css2?family=Open+Sans:ital,wght@0,400;0,600;1,400&family=Michroma&display=swap">
<style>
  :root {
    --board: #3b3b3d;
    --card-white: #ffffff;
    --card-black: #050505;
    --panel-deep: #0d1a6b;
    --panel-mid: #24409e;
    --brand-blue: #1f4f9c;
    --brand-gold: #e9b324;
    --name-gold: #f4cc2a;
    --panel-text: #dfe6f5;
    --label: #e8e8e8;
    --on-black: #d7a52a;
  }
  * { box-sizing: border-box; margin: 0; padding: 0; }
  html, body { width: 1200px; height: 806px; overflow: hidden; background: var(--board); }
  .board { position: relative; width: 1200px; height: 806px; }

  .card {
    position: absolute; width: 537px; height: 338px; overflow: hidden;
    box-shadow: 0 4px 10px rgba(0,0,0,.5);
  }
  .card--light { background: var(--card-white); }
  .card--dark { background: var(--card-black); }
  .pos-front-a { left: 34px; top: 36px; }
  .pos-front-b { left: 629px; top: 36px; }
  .pos-back-a { left: 34px; top: 418px; }
  .pos-back-b { left: 629px; top: 418px; }

  .card__brand-zone {
    position: absolute; left: 0; top: 0; bottom: 0; width: 281px;
    display: flex; flex-direction: column; align-items: center; justify-content: center;
    padding: 0 10px;
  }
  .card--back .card__brand-zone { width: 100%; }

  .brand-mark { display: flex; align-items: center; gap: 7px; }
  .brand-mark__square { flex: none; width: 11px; height: 11px; background: var(--brand-gold); }
  .brand-name {
    font-family: "Open Sans", sans-serif; font-weight: 400; font-size: 12.5px;
    color: var(--brand-blue); white-space: nowrap;
  }
  .card--dark .brand-name { color: var(--on-black); }
  .brand-tagline {
    margin-top: 6px; font-family: "Open Sans", sans-serif; font-size: 8.5px;
    color: var(--brand-blue); letter-spacing: 1px; white-space: nowrap;
  }
  .card--dark .brand-tagline { color: var(--on-black); }

  .card__contact-panel {
    position: absolute; left: 281px; top: 0; right: 0; bottom: 0;
    background: radial-gradient(ellipse at 60% 45%, var(--panel-mid) 0%, var(--panel-deep) 85%);
    padding: 42px 14px 0 22px; font-family: "Open Sans", sans-serif; color: var(--panel-text);
  }
  .contact__name { font-size: 14px; font-weight: 600; color: var(--name-gold); }
  .contact__role { font-size: 11px; font-style: italic; margin-top: 1px; }
  .contact__list { list-style: none; margin-top: 16px; }
  .contact__item { display: flex; align-items: flex-start; gap: 8px; font-size: 10.5px; line-height: 1.35; margin-bottom: 8px; white-space: nowrap; }
  .contact__item svg { flex: none; margin-top: 1px; }
  .contact__list--phones .contact__item { margin-bottom: 4px; }

  .label {
    position: absolute; width: 537px; text-align: center;
    font-family: "Michroma", sans-serif; font-size: 15px; color: var(--label); letter-spacing: 1px;
  }
  .label--front { top: 384px; }
  .label--back { top: 770px; }
  .label--a { left: 34px; }
  .label--b { left: 629px; }
</style>
</head>
<body>
<main class="board">

  <section class="card card--light card--front pos-front-a">
    <div class="card__brand-zone">
      <div class="brand-mark"><span class="brand-mark__square"></span><span class="brand-name">R &amp; M Holdings of Fairhaven, LLC</span></div>
      <p class="brand-tagline">Steady Care for Every Home</p>
    </div>
    <div class="card__contact-panel">
      <p class="contact__name">Bertram Lasko</p>
      <p class="contact__role">Property Manager</p>
      <ul class="contact__list">
        <li class="contact__item"><svg width="11" height="11" viewBox="0 0 12 12"><circle cx="6" cy="6" r="6" fill="#e9b324"/><path d="M6 2.5a2.2 2.2 0 0 0-2.2 2.2C3.8 6.5 6 9.5 6 9.5s2.2-3 2.2-4.8A2.2 2.2 0 0 0 6 2.5z" fill="#0d1a6b"/></svg><span>P.O. Box 38216<br>Larkmoor, VT 05921</span></li>
      </ul>
      <ul class="contact__list contact__list--phones">
        <li class="contact__item"><svg width="11" height="11" viewBox="0 0 12 12"><circle cx="6" cy="6" r="6" fill="#e9b324"/><rect x="4" y="2.5" width="4" height="7" rx="1" fill="#0d1a6b"/></svg><span>(555) 014-2871</span></li>
        <li class="contact__item"><svg width="11" height="11" viewBox="0 0 12 12"><circle cx="6" cy="6" r="6" fill="#e9b324"/><rect x="4" y="2.5" width="4" height="7" rx="1" fill="#0d1a6b"/></svg><span>(555) 014-3390</span></li>
        <li class="contact__item"><svg width="11" height="11" viewBox="0 0 12 12"><circle cx="6" cy="6" r="6" fill="#e9b324"/><rect x="3" y="3.5" width="6" height="5" fill="#0d1a6b"/></svg><span>(555) 014-5162</span></li>
      </ul>
      <ul class="contact__list">
        <li class="contact__item"><svg width="11" height="11" viewBox="0 0 12 12"><circle cx="6" cy="6" r="6" fill="#e9b324"/><rect x="3" y="3.8" width="6" height="4.4" fill="none" stroke="#0d1a6b" stroke-width="1"/><path d="M3 4l3 2.2L9 4" fill="none" stroke="#0d1a6b" stroke-width="1"/></svg><span>rmholdings2011@quillpost.example</span></li>
      </ul>
    </div>
  </section>

  <section class="card card--dark card--front pos-front-b">
    <div class="card__brand-zone">
      <div class="brand-mark"><span class="brand-mark__square"></span><span class="brand-name">R &amp; M Holdings of Fairhaven, LLC</span></div>
      <p class="brand-tagline">Steady Care for Every Home</p>
    </div>
    <div class="card__contact-panel">
      <p class="contact__name">Bertram Lasko</p>
      <p class="contact__role">Property Manager</p>
      <ul class="contact__list">
        <li class="contact__item"><svg width="11" height="11" viewBox="0 0 12 12"><circle cx="6" cy="6" r="6" fill="#e9b324"/><path d="M6 2.5a2.2 2.2 0 0 0-2.2 2.2C3.8 6.5 6 9.5 6 9.5s2.2-3 2.2-4.8A2.2 2.2 0 0 0 6 2.5z" fill="#0d1a6b"/></svg><span>P.O. Box 38216<br>Larkmoor, VT 05921</span></li>
      </ul>
      <ul class="contact__list contact__list--phones">
        <li class="contact__item"><svg width="11" height="11" viewBox="0 0 12 12"><circle cx="6" cy="6" r="6" fill="#e9b324"/><rect x="4" y="2.5" width="4" height="7" rx="1" fill="#0d1a6b"/></svg><span>(555) 014-2871</span></li>
        <li class="contact__item"><svg width="11" height="11" viewBox="0 0 12 12"><circle cx="6" cy="6" r="6" fill="#e9b324"/><rect x="4" y="2.5" width="4" height="7" rx="1" fill="#0d1a6b"/></svg><span>(555) 014-3390</span></li>
        <li class="contact__item"><svg width="11" height="11" viewBox="0 0 12 12"><circle cx="6" cy="6" r="6" fill="#e9b324"/><rect x="3" y="3.5" width="6" height="5" fill="#0d1a6b"/></svg><span>(555) 014-5162</span></li>
      </ul>
      <ul class="contact__list">
        <li class="contact__item"><svg width="11" height="11" viewBox="0 0 12 12"><circle cx="6" cy="6" r="6" fill="#e9b324"/><rect x="3" y="3.8" width="6" height="4.4" fill="none" stroke="#0d1a6b" stroke-width="1"/><path d="M3 4l3 2.2L9 4" fill="none" stroke="#0d1a6b" stroke-width="1"/></svg><span>rmholdings2011@quillpost.example</span></li>
      </ul>
    </div>
  </section>

  <section class="card card--light card--back pos-back-a">
    <div class="card__brand-zone">
      <div class="brand-mark"><span class="brand-mark__square"></span><span class="brand-name">R &amp; M Holdings of Fairhaven, LLC</span></div>
      <p class="brand-tagline">Steady Care for Every Home</p>
    </div>
  </section>

  <section class="card card--dark card--back pos-back-b">
    <div class="card__brand-zone">
      <div class="brand-mark"><span class="brand-mark__square"></span><span class="brand-name">R &amp; M Holdings of Fairhaven, LLC</span></div>
      <p class="brand-tagline">Steady Care for Every Home</p>
    </div>
  </section>

  <p class="label label--front label--a">Business Card Front A</p>
  <p class="label label--front label--b">Business Card Front B</p>
  <p class="label label--back label--a">Business Card Back A</p>
  <p class="label label--back label--b">Business Card Back B</p>
</main>
</body>
</html>
```